Quillon Maison Wood Fired Pizza business card design

I have a logo and need an eye catching design that will get me noticed.
My business is wood fired pizza. I want a bold design that will make our customers remember us and the food that we serve. Work with the colors of our logo and texts. Maybe add designs that lend to what or how pizza is made using our wood fired oven?

Target Market(s)

Foodies!

Contact Information for Business Card

Quillon Maison Wood Fired Pizza
Our slogan is Fast. Fresh. Handcrafted
Catering for all events

Requirements
Must have
• Dana Porrick
Telephone 570 555 0183
website www.getquillon.example
Facebook @getquillonpizza maybe use the facebook logo next to it
Instagram getquillonpizza maybe use the instagram logo next to it
Catering for all events
Nice to have
• Maybe pizza peels, pizza cutters? Wood? Fired wood? Using our flame in the background?
Please work with different colored text so each sentence stands out? A themed color for facebook?
Maybe work with the colors within our logo?
Please try to use the our quillon font, but not a must have.

```html
<!DOCTYPE html>
<html lang="en">
<head>
<meta charset="utf-8">
<title>Quillon Maison Wood Fired Pizza – Business Card</title>
<link href="https://fonts.googleapis.com/css2?family=Exo+2:wght@500;600;700&family=Open+Sans:wght@400&display=swap" rel="stylesheet">
<style>
  :root {
    --stage: #d4d5d7;
    --card: #231f20;
    --flame-red: #d0323d;
    --ember-orange: #f0922b;
    --ink-light: #ffffff;
    --photo-hot: #f6b35a;
    --photo-mid: #b8692a;
    --photo-dark: #3a1d0c;
  }
  * { box-sizing: border-box; margin: 0; padding: 0; }
  html, body {
    width: 1200px; height: 1167px; overflow: hidden;
    background: var(--stage);
  }
  .card {
    position: absolute; left: 341px; width: 541px; height: 309px;
    border-radius: 36px; background: var(--card); overflow: hidden;
  }
  .card--front { top: 227px; }
  .card--back { top: 606px; }

  .slogan {
    position: absolute; left: 0; right: 0; text-align: center;
    font-family: "Exo 2", sans-serif; font-weight: 500;
    font-size: 22px; line-height: 26px; letter-spacing: 1.2px;
    color: var(--ember-orange);
  }
  .slogan--top { top: 13px; }
  .slogan--bottom { top: 260px; }

  .brand {
    position: absolute; left: 0; right: 0;
    display: flex; flex-direction: column; align-items: center;
  }
  .brand__dot {
    display: block; border-radius: 50%; background: var(--flame-red);
  }
  .brand__rule {
    display: block; height: 2px; background: var(--ember-orange);
  }
  .brand__descriptor {
    font-family: "Exo 2", sans-serif; font-weight: 600;
    color: var(--ink-light); letter-spacing: 1.2px; text-transform: uppercase;
    line-height: 1;
  }
  .brand__name {
    font-family: "Exo 2", sans-serif; font-weight: 700;
    color: var(--ink-light); letter-spacing: 2px; text-transform: uppercase;
    line-height: 1;
  }

  .card--front .brand { top: 78px; }
  .card--front .brand__dot { width: 96px; height: 96px; }
  .card--front .brand__rule { width: 136px; margin-top: 8px; }
  .card--front .brand__descriptor { font-size: 9px; margin-top: 7px; }
  .card--front .brand__name { font-size: 28px; margin-top: 5px; }
  .card--front .brand__rule--under { width: 136px; height: 1px; margin-top: 6px; }

  .oven-photo {
    position: absolute; left: 0; top: 0; width: 270px; height: 100%;
    background: radial-gradient(ellipse at 45% 30%, var(--photo-hot) 0%, var(--photo-mid) 45%, var(--photo-dark) 100%);
  }
  .info-panel {
    position: absolute; left: 270px; top: 0; right: 0; height: 100%;
  }
  .info-panel .brand { top: 24px; }
  .info-panel .brand__dot { width: 64px; height: 64px; }
  .info-panel .brand__rule { width: 86px; height: 1.5px; margin-top: 5px; }
  .info-panel .brand__descriptor { font-size: 6px; margin-top: 4px; letter-spacing: 0.8px; }
  .info-panel .brand__name { font-size: 17px; letter-spacing: 1.5px; margin-top: 3px; }
  .info-panel .brand__rule--under { width: 86px; height: 1px; margin-top: 4px; }

  .person-name {
    position: absolute; left: 0; right: 0; top: 148px; text-align: center;
    font-family: "Exo 2", sans-serif; font-weight: 600; font-size: 24px;
    line-height: 28px; color: var(--ember-orange); text-transform: uppercase;
  }
  .contact-list { position: absolute; left: 66px; top: 183px; list-style: none; }
  .contact-list li {
    display: flex; align-items: center; height: 22.7px;
    font-family: "Open Sans", sans-serif; font-size: 12px; color: var(--ink-light);
  }
  .contact-icon {
    width: 15px; height: 15px; border-radius: 50%; background: var(--flame-red);
    margin-right: 5px; flex: none; display: flex; align-items: center; justify-content: center;
  }
  .contact-icon svg { width: 9px; height: 9px; }
</style>
</head>
<body>

<section class="card card--front">
  <p class="slogan slogan--top">FAST . FRESH . HANDCRAFTED</p>
  <div class="brand">
    <span class="brand__dot"></span>
    <span class="brand__rule"></span>
    <p class="brand__descriptor">Wood Fired Pizza</p>
    <p class="brand__name">Quillon Maison</p>
    <span class="brand__rule brand__rule--under"></span>
  </div>
  <p class="slogan slogan--bottom">CATERING . FOR . ALL . EVENTS</p>
</section>

<section class="card card--back">
  <div class="oven-photo" role="img" aria-label="Photo of a pepperoni pizza in front of burning logs in a wood fired oven"></div>
  <div class="info-panel">
    <div class="brand">
      <span class="brand__dot"></span>
      <span class="brand__rule"></span>
      <p class="brand__descriptor">Wood Fired Pizza</p>
      <p class="brand__name">Quillon Maison</p>
      <span class="brand__rule brand__rule--under"></span>
    </div>
    <p class="person-name">Dana Porrick</p>
    <ul class="contact-list">
      <li>
        <span class="contact-icon">
          <svg viewBox="0 0 24 24"><path fill="#fff" d="M6.6 10.8a15 15 0 0 0 6.6 6.6l2.2-2.2c.3-.3.7-.4 1-.2 1.1.4 2.3.6 3.6.6.6 0 1 .4 1 1V20c0 .6-.4 1-1 1A17 17 0 0 1 3 4c0-.6.4-1 1-1h3.5c.6 0 1 .4 1 1 0 1.3.2 2.5.6 3.6.1.3 0 .7-.2 1z"/></svg>
        </span>570 555 0183
      </li>
      <li>
        <span class="contact-icon">
          <svg viewBox="0 0 24 24" fill="none" stroke="#fff" stroke-width="2"><circle cx="12" cy="12" r="9"/><path d="M3 12h18M12 3c3 3 3 15 0 18M12 3c-3 3-3 15 0 18"/></svg>
        </span>www.getquillon.example
      </li>
      <li><span class="contact-icon"></span>@getquillonpizza</li>
      <li><span class="contact-icon"></span>getquillonpizza</li>
    </ul>
  </div>
</section>

</body>
</html>
```